Catering company looking to promote business

We need a flyer design for our company named "Berry Good Bites." We cater/deliver açaí bowls and smoothies.

The objective of this flyer is to let companies know that we are taking açaí bowls and smoothie orders and they can be delivered to them.

Some key points we would like on the flyer:
- Photo of açaí bowl and smoothie
- Menu w/ pricing
- "No hidden delivery fees"
- 5 bowl or smoothie minimum
- Online ordering through website:
https://shopkiosk.example/store/berrygoodbites
- For the month of February --> Get one free topping and drizzle!
- FRIDAY DELIVERIES ONLY
- Questions? Call (555) 417-9832
- social media chatterbook & snapgram @bgbites
- website www.berrygoodbites.example

font - hello beautiful

Target Market(s)

Juice, smoothies, açaí bowls

Industry/Entity Type

Business

Font styles to use
Other font styles liked:
• Hello Beautiful

Colors
a64599
b768aa
d3a5cc
eedced
f7f1f7
9bcb3c

Requirements
Must have
• Please match logo, fonts, color schemes, etc.

```html
<!DOCTYPE html>
<html lang="en">
<head>
<meta charset="utf-8">
<title>Berry Good Bites – Açaí Catering Flyer</title>
<link href="https://fonts.googleapis.com/css2?family=Oswald:wght@300;400&family=Great+Vibes&family=Libre+Baskerville:wght@700&family=Open+Sans:wght@400&display=swap" rel="stylesheet">
<style>
  :root {
    --plum: #a64599;
    --orchid: #b768aa;
    --lilac: #d3a5cc;
    --blush: #f9dfec;
    --mist: #f7f1f7;
    --leaf: #9bcb3c;
    --violet: #6a4a9e;
    --deep: #4f3285;
    --ink: #2a2230;
    --stage: #4a4a4a;
  }
  html, body {
    margin: 0;
    width: 1200px;
    height: 1200px;
    overflow: hidden;
    background: var(--stage);
  }
  .flyer {
    position: absolute;
    left: 232px;
    top: 81px;
    width: 736px;
    height: 1037px;
    background: var(--blush);
    overflow: hidden;
  }
  .flyer svg { display: block; }
  .condensed { font-family: "Oswald", "Arial Narrow", sans-serif; font-weight: 300; }
  .script { font-family: "Great Vibes", cursive; fill: var(--violet); }
  .serif-bold { font-family: "Libre Baskerville", Georgia, serif; font-weight: 700; }
  .sans { font-family: "Open Sans", Arial, sans-serif; }
  .heading-purple { fill: var(--violet); }
  .body-ink { fill: var(--ink); }
  .on-purple { fill: #ffffff; }
  .brand-name { font-family: "Oswald", "Arial Narrow", sans-serif; font-weight: 400; fill: var(--plum); }
</style>
</head>
<body>
<div class="flyer">
<svg width="736" height="1037" viewBox="0 0 736 1037" xmlns="http://www.w3.org/2000/svg">
  <defs>
    <linearGradient id="fadedPhoto" x1="0" y1="0" x2="1" y2="1">
      <stop offset="0" stop-color="#d9c9d4"/>
      <stop offset="1" stop-color="#efdfe8"/>
    </linearGradient>
    <linearGradient id="bowlPhoto" x1="0" y1="0" x2="0" y2="1">
      <stop offset="0" stop-color="#d8dde6"/>
      <stop offset="0.35" stop-color="#c94a55"/>
      <stop offset="0.7" stop-color="#a84b5a"/>
      <stop offset="1" stop-color="#5b3a4a"/>
    </linearGradient>
    <radialGradient id="miniBowl" cx="0.5" cy="0.5" r="0.5">
      <stop offset="0" stop-color="#5a4a8a"/>
      <stop offset="0.6" stop-color="#d4565e"/>
      <stop offset="1" stop-color="#2f4a5a"/>
    </radialGradient>
    <linearGradient id="ribbon" x1="0" y1="0" x2="1" y2="0">
      <stop offset="0" stop-color="#d3a5cc"/>
      <stop offset="0.5" stop-color="#f7f1f7"/>
      <stop offset="1" stop-color="#d3a5cc"/>
    </linearGradient>
    <linearGradient id="footerBand" x1="0" y1="0" x2="0" y2="1">
      <stop offset="0" stop-color="#3e2a6a"/>
      <stop offset="1" stop-color="#6a4a9e"/>
    </linearGradient>
  </defs>

  <!-- faded hero photo area -->
  <rect class="hero-faded" x="0" y="0" width="356" height="264" fill="url(#fadedPhoto)" role="img" aria-label="Faded photo of an açaí bowl"/>

  <!-- brand mark area -->
  <g class="brand">
    <circle cx="82" cy="110" r="9" fill="var(--orchid)"/>
    <text class="brand-name" x="98" y="118" font-size="24">Berry Good Bites</text>
  </g>

  <!-- swoosh from top -->
  <path class="swoosh" d="M318 0 L356 0 C378 150 470 290 600 355 L736 430 L736 492 L585 405 C430 330 336 190 318 0 Z" fill="var(--orchid)"/>
  <path d="M318 0 C336 190 430 330 585 405 L736 492 L736 482 L588 396 C438 322 344 186 326 0 Z" fill="var(--deep)"/>

  <!-- açaí bowl photo -->
  <path class="hero-photo" d="M420 0 L736 0 L736 416 L610 360 C520 318 470 240 440 120 Z" fill="url(#bowlPhoto)" role="img" aria-label="Photo of two açaí bowls topped with strawberries, blueberries and granola"/>

  <!-- swoosh from left -->
  <path class="swoosh" d="M0 266 C90 370 260 440 450 452 L450 468 C250 468 90 410 0 340 Z" fill="var(--orchid)"/>
  <path d="M0 266 C90 370 260 440 450 452 L450 446 C262 434 96 362 0 255 Z" fill="var(--deep)"/>

  <!-- starburst -->
  <polygon class="starburst" fill="var(--orchid)" stroke="var(--deep)" stroke-width="2"
    points="496,290 518,334 566,308 556,358 610,360 572,396 618,424 566,436 590,484 538,470 530,522 500,480 468,512 462,462 412,470 436,426 384,404 432,388 396,346 448,354 440,302 478,332"/>
  <g transform="translate(500 412) rotate(-27)" class="sans on-purple" font-size="24" text-anchor="middle">
    <text x="0" y="-24">NO HIDDEN</text>
    <text x="6" y="6">DELIVERY</text>
    <text x="16" y="36">FEES</text>
  </g>

  <!-- ordering info -->
  <text class="condensed heading-purple" x="20" y="230" font-size="21">ONLINE ORDERING THROUGH WEBSITE:</text>
  <text class="condensed body-ink" x="20" y="262" font-size="21">https://shopkiosk.example/store/berrygoodbites</text>
  <text class="condensed body-ink" x="72" y="297" font-size="27">For the month of February --&gt;</text>
  <text class="condensed body-ink" x="112" y="331" font-size="27">Get one free topping and drizzle!</text>

  <!-- main item -->
  <text class="script" x="28" y="498" font-size="52">Açaí Bowl&#160;&#160;$9.00</text>
  <text class="condensed body-ink" x="26" y="540" font-size="21">açaí SORBET TOPPED WITH GRANOLA, BANANAS, STRAWBERRIES, BLUEBERRIES,</text>
  <text class="condensed body-ink" x="26" y="574" font-size="21">COCONUT SHAVINGS AND DRIZZLED WITH HONEY</text>

  <text class="script" x="272" y="632" font-size="46">Want to add something extra?</text>

  <!-- questions panel -->
  <rect class="questions-panel" x="38" y="658" width="198" height="300" rx="10" fill="var(--orchid)"/>
  <path d="M16 714 L38 728 L38 714 Z M258 714 L236 728 L236 714 Z" fill="var(--deep)"/>
  <rect x="16" y="678" width="242" height="36" rx="8" fill="url(#ribbon)"/>
  <text class="serif-bold body-ink" x="137" y="704" font-size="21" text-anchor="middle">QUESTIONS ??</text>
  <g class="condensed on-purple" text-anchor="middle" font-size="21">
    <text x="136" y="738">ORDER</text>
    <text x="136" y="766">5 BOWL OR</text>
    <text x="136" y="795">SMOOTHIE MINIMUM</text>
    <text x="136" y="830" font-size="15">snapgram · chatterbook</text>
    <text x="136" y="860">@bgbites</text>
    <text x="136" y="902" font-size="23"><tspan font-weight="400">Call</tspan> (555) 417-9832</text>
  </g>

  <!-- menu extras -->
  <g class="menu-extras" text-anchor="middle">
    <circle cx="356" cy="694" r="34" fill="url(#miniBowl)" stroke="#2f4a5a" stroke-width="2" role="img" aria-label="Top view of an açaí bowl"/>
    <circle cx="504" cy="694" r="34" fill="url(#miniBowl)" stroke="#2f4a5a" stroke-width="2" role="img" aria-label="Top view of an açaí bowl"/>
    <circle cx="650" cy="694" r="34" fill="url(#miniBowl)" stroke="#2f4a5a" stroke-width="2" role="img" aria-label="Top view of an açaí bowl"/>

    <g class="condensed heading-purple" font-size="22">
      <text x="356" y="760">FRUITS</text>
      <text x="504" y="760">TOPPINGS</text>
      <text x="650" y="760">DRIZZLE</text>
      <text x="356" y="792">$1.00</text>
      <text x="504" y="792">0.50¢</text>
      <text x="650" y="792">0.50¢</text>
    </g>
    <g class="condensed body-ink" font-size="14">
      <text x="356" y="820">Bananas</text>
      <text x="356" y="839">Strawberries</text>
      <text x="356" y="858">Blueberries</text>
      <text x="504" y="818">Almonds, chia seeds</text>
      <text x="504" y="836">hemp seeds, cacao nibs</text>
      <text x="504" y="854">quinoa puffs, coconut shavings</text>
      <text x="504" y="872">GRANOLA</text>
      <text x="650" y="820">Peanut Butter</text>
      <text x="650" y="839">Almond Butter</text>
      <text x="650" y="858">Honey Agave</text>
    </g>
  </g>

  <g class="sans heading-purple" font-size="25">
    <text x="250" y="904">FRIDAY</text>
    <text x="250" y="937">DELIVERIES ONLY</text>
  </g>

  <!-- torn footer band -->
  <path class="footer-band" d="M0 930 L22 926 L34 934 L52 928 L66 938 L88 934 L104 946 L120 940 L138 948 L154 940 L172 944 L186 936 L204 942 L220 938 L236 948 L252 944 L268 956 L288 950 L306 958 L322 952 L340 962 L358 954 L376 956 L392 950 L410 952 L428 946 L446 952 L462 946 L480 954 L498 948 L516 946 L534 940 L552 946 L570 938 L586 944 L604 936 L622 942 L640 932 L658 938 L676 930 L694 936 L712 928 L736 932 L736 1037 L0 1037 Z"
    fill="url(#footerBand)" stroke="#ffffff" stroke-width="4"/>
  <text class="condensed on-purple" x="368" y="1012" font-size="30" text-anchor="middle" letter-spacing="2" font-weight="400">www.berrygoodbites.example</text>
</svg>
</div>
</body>
</html>
```